Brightmoor Snacks needs a label design

I need a design for a label on a snacks company packets/containers.
we manufacture Indian snacks.
The label should be green in color and must have background image of indian snacks on it.
Updates

Project Deadline Extended
Reason: Extension of 5 days due to lack of design submission by Designers

Target Market(s)

Groceries Supermarkets

Industry/Entity Type

Food Store

Font styles to use
Script

Colors
9bcb3c

Requirements
Must have
• Similar setup as Tavlor Snacks see attachment below of Tavlors Packet
Nice to have
• Indian snacks in background in dull colors but visible image as I would print ingredients list and other information such as nutritional info
Should not have

```html
<!DOCTYPE html>
<html lang="en">
<head>
<meta charset="utf-8">
<title>Brightmoor Hot Mix Bhuja Label</title>
<link rel="stylesheet" href="https://fonts.googleapis.com/css2?family=Open+Sans:wght@400;600;700&family=Oswald:wght@500&family=Roboto+Condensed:wght@400;700&display=swap">
<style>
  :root {
    --page: #efefea;
    --label-green: #2d8b3c;
    --label-green-dark: #1f6e2e;
    --brand-box: #2a8c3a;
    --brand-box-edge: #5fae4a;
    --brand-yellow: #f5e51b;
    --title-green: #1d6a2c;
    --snack-light: #e2c690;
    --snack-dark: #c2914f;
    --band-red: #d6232a;
    --band-red-dark: #b81c22;
    --band-orange: #f08a1c;
    --white: #ffffff;
    --ink: #1a1a1a;
    --claim-red: #d8262c;
  }
  html, body {
    margin: 0;
    padding: 0;
    width: 1200px;
    height: 1200px;
    overflow: hidden;
    background: var(--page);
  }
  .canvas {
    position: relative;
    width: 1200px;
    height: 1200px;
  }
  .label {
    position: absolute;
    left: 40px;
    top: 350px;
    width: 1120px;
    height: 501px;
    filter: drop-shadow(0 6px 14px rgba(0,0,0,0.18));
  }
  .text-sans { font-family: "Open Sans", sans-serif; }
  .text-cond { font-family: "Roboto Condensed", sans-serif; }
  .claim { font-family: "Oswald", sans-serif; font-weight: 500; }
  .brand-name { font-family: "Open Sans", sans-serif; font-weight: 700; }
</style>
</head>
<body>
<main class="canvas">
  <svg class="label" viewBox="0 0 832 372" xmlns="http://www.w3.org/2000/svg">
    <defs>
      <linearGradient id="snack-fill" x1="0" y1="0" x2="1" y2="1">
        <stop offset="0" stop-color="var(--snack-light)"/>
        <stop offset="0.5" stop-color="#d6b177"/>
        <stop offset="1" stop-color="var(--snack-dark)"/>
      </linearGradient>
      <linearGradient id="red-band" x1="0" y1="0" x2="0" y2="1">
        <stop offset="0" stop-color="var(--band-red)"/>
        <stop offset="1" stop-color="var(--band-red-dark)"/>
      </linearGradient>
      <clipPath id="label-shape">
        <rect x="0" y="0" width="832" height="372" rx="18"/>
      </clipPath>
    </defs>

    <g clip-path="url(#label-shape)">
      <!-- base -->
      <rect class="label-base" x="0" y="0" width="832" height="372" fill="var(--label-green)"/>

      <!-- snack photo area -->
      <rect class="snack-photo" x="10" y="10" width="812" height="198" rx="12" fill="url(#snack-fill)"
            role="img" aria-label="Photo of Indian hot mix bhuja snacks: sev, peanuts and chickpeas"/>

      <!-- red info band -->
      <rect class="info-band" x="0" y="275" width="832" height="97" fill="url(#red-band)"/>
      <rect class="info-band-stripe" x="0" y="275" width="832" height="9" fill="var(--band-orange)"/>
    </g>

    <!-- gluten free claim -->
    <g class="claim-gluten-free">
      <rect x="24" y="40" width="188" height="37" rx="4" fill="var(--white)"/>
      <circle cx="43" cy="58.5" r="13" fill="var(--claim-red)"/>
      <text class="claim" x="62" y="71" font-size="29" fill="var(--claim-red)">GLUTEN FREE</text>
    </g>

    <!-- brand box -->
    <g class="brand-box">
      <rect x="230" y="22" width="372" height="128" rx="14" fill="var(--brand-box)" stroke="var(--brand-box-edge)" stroke-width="3"/>
      <text class="brand-name" x="416" y="106" font-size="58" fill="var(--brand-yellow)" text-anchor="middle">Brightmoor</text>
    </g>

    <!-- net weight -->
    <text class="text-sans net-weight" x="810" y="46" font-size="20" font-weight="600" fill="var(--white)" text-anchor="end">350 Grams</text>

    <!-- product name -->
    <text class="text-sans product-name" x="417" y="198" font-size="40" font-weight="700" fill="var(--title-green)" text-anchor="middle">HOT MIX BHUJA</text>

    <!-- ingredients -->
    <text class="text-sans ingredients" x="12" y="247" font-size="27" font-weight="600" fill="var(--white)">Ingredients : Nuts, Peas, Corn, Snack. etc.</text>

    <!-- origin badge (plain shape) -->
    <rect class="origin-badge" x="14" y="290" width="74" height="70" rx="3" fill="var(--white)"/>

    <!-- company -->
    <text class="text-sans company-name" x="116" y="327" font-size="24" font-weight="700" fill="var(--white)">BRIGHTMOOR FOODS PTY. LTD.</text>
    <text class="text-sans company-line" x="116" y="350" font-size="18.5" fill="var(--white)">Lorem ipsum dolor sit amet, sea errem vocibus</text>

    <!-- nutrition facts panel -->
    <g class="nutrition-facts text-cond" fill="var(--ink)">
      <rect x="610" y="220" width="200" height="138" fill="var(--white)"/>
      <text x="618" y="245" font-size="22" font-weight="700" font-family="Open Sans, sans-serif">Nutrition Facts</text>
      <rect x="616" y="250" width="188" height="2.5"/>
      <text x="618" y="261" font-size="8">Amount Per Serving</text>
      <rect x="616" y="264" width="188" height="0.8"/>
      <text x="618" y="275" font-size="8">Calories 45</text>
      <text x="804" y="275" font-size="8" text-anchor="end">Calories from Fat 27g</text>
      <rect x="616" y="279" width="188" height="2"/>
      <text x="804" y="291" font-size="8" text-anchor="end">% Daily Value*</text>
      <rect x="616" y="294" width="188" height="0.8"/>
      <text x="618" y="302" font-size="8">Total Fat 301g</text>
      <text x="798" y="302" font-size="8" text-anchor="end">5%</text>
      <text x="627" y="313" font-size="8">Saturated Fat 0.44g</text>
      <text x="798" y="313" font-size="8" text-anchor="end">2%</text>
      <text x="627" y="324" font-size="8">Trans Fat 0g</text>
      <rect x="616" y="327" width="188" height="0.8"/>
      <text x="618" y="334" font-size="8">Cholesterol   0mg</text>
      <text x="798" y="334" font-size="8" text-anchor="end">0%</text>
      <text x="618" y="345" font-size="8">Sodium 17mg</text>
      <text x="798" y="345" font-size="8" text-anchor="end">1%</text>
    </g>
  </svg>
</main>
</body>
</html>
```